Dentistry Office

We want a new design for a Dentist's office website.

The theme is: "We provide high quality, state-of-the-art, dental care in a comfortable, caring environment."

The site currently has a menu on the left of the page with about 40 items on it. There is a great deal of textual content on each page, plus several illustrations.

We want to do this using CSS, so we need specifications in the CSS for all possible elements. The CSS needs to be named in a logical manner for easy use.

Every dentist on the planet seems to use lots of Flash. We don't want to because it is so distracting. We are looking for an elegant solution targeting 24-55 age group, but not excluding anyone.

The following (from another dentist's site) can give you a taste of what we want to communicate on the site:

"After 20 years of teaching dentists how to refine their technique and many years of writing textbooks, I currently devote my time to my office and the hands-on practice of dentistry. I'd like to welcome you personally to my dental practice, and I invite you to meet my highly experienced team of professionals.

"We have offered complete dental care of the highest quality since 1978. We provide Preventive Services, Tooth Whitening and Cosmetic Dentistry for a beautiful smile, Endodontics (root canal treatment) to treat painful teeth, Sedation Dentistry so you can relax, and Dental Implants to restore what is missing. We offer total care.

"Our approach to your health is simple: We use our education, experience and dedication to provide every patient with superior dental care.

"This passion for excellence is not just a goal, but a standard every member of our team holds.

"We also pride ourselves with our state of the art procedures, training and technology. This includes creating a beautiful smile using techniques that preserve as much of the original tooth as possible.

"Our abilities are renowned throughout the dental profession and I hope if you have any questions you will contact us by an e-mail note, by phone or just by dropping by."

Keep in mind the screen shape and dimensions. Your design needs to work in the normal screen proportions, regardless of how it looks when you post it here. Scrolling is OK, but the first impression needs to work.

Keep in mind that there will be about 250 words, or more, on each page.

Competitors web sites:

http://www.brevalkoortho.example/

http://www.quimbelfieldcare.example/

http://www.grinsatdoverellclinic.example/

http://www.trunwickfamilydentalcare.example/

http://www.morvanhaledental.example/

http://www.ubrigandental.example/

We need to compete with these.

Target Market(s)

Generally adults seeking the most experienced and comfortable-to-be-with dentist.

Industry/Entity Type

Training

Requirements
Must have
• Must stand apart from other dentists.
• Must be elegant.
• Must have a horizontal menu structure across all columns, NOT a vertical that requires scrolling, no popout, pop down, etc. menus.
• We are looking for something special.
• Do not waste your time or ours putting up templates and things you have used before.
• Personally, I do not see how someone outside the US can understand the northern California dental market. But you are welcome to try.
Should not have
• Flash or graphics that move
• The look of a template
• Folksy fonts
• Looks like you used it 20 times before

```html
<!DOCTYPE html>
<html lang="en">
<head>
<meta charset="utf-8">
<title>DrVantrell – Dental Care</title>
<link href="https://fonts.googleapis.com/css2?family=Gelasio:wght@400&family=Noto+Sans:wght@400&display=swap" rel="stylesheet">
<style>
:root{
  --page-bg:#eae8e9;
  --navy:#0b4568;
  --navy-deep:#073a59;
  --heading:#0d3f62;
  --rule:#b9c7d0;
  --text:#5a5f66;
  --muted:#8a8a8a;
  --accent:#5cb6d2;
  --white:#ffffff;
  --serif:"Gelasio", Georgia, serif;
  --sans:"Noto Sans", Verdana, sans-serif;
}
*{margin:0;padding:0;box-sizing:border-box}
html,body{width:1200px;height:1200px;overflow:hidden}
body{position:relative;background:var(--page-bg);font-family:var(--sans);color:var(--text)}
a{color:inherit;text-decoration:none}
.brand{position:absolute;left:115px;top:18px;font-family:var(--serif);font-size:56px;color:var(--navy);line-height:1;letter-spacing:-1px}
.masthead{position:absolute;left:0;top:74px;width:1200px;height:133px;background:linear-gradient(var(--navy),var(--navy-deep))}
.masthead-rule{position:absolute;left:0;top:207px;width:1200px;height:4px;background:var(--rule)}
.main-nav{position:absolute;left:115px;top:124px;display:flex;font-family:var(--serif);font-size:23px;color:#e9f1f6}
.main-nav a{border-bottom:3px solid #0f5b82;padding-bottom:2px}
.main-nav a.is-current{border-color:var(--accent)}
.main-nav .sep{margin:0 12px;color:#cfe0ea}
.intro{position:absolute;left:123px;top:242px;width:954px;height:262px;background:var(--white);padding:24px 28px 0 27px;font-family:var(--serif);font-size:17.4px;line-height:24px;color:var(--muted);text-align:justify}
.intro-photo{float:left;width:130px;height:97px;margin:4px 13px 6px 0;background:linear-gradient(#9a9a9a,#4a4a4a)}
.intro p+p{margin-top:18px;clear:both}
.section-rule{position:absolute;left:100px;top:504px;width:997px;height:1px;background:#d8d6d7}
.pointer{position:absolute;left:510px;top:504px}
.col{position:absolute;top:544px}
.col h2{font-family:var(--serif);font-weight:400;font-size:20px;color:var(--heading);margin-bottom:7px}
.col li{list-style:none;font-size:12.5px;line-height:20px}
.visit{position:absolute;left:500px;top:628px;width:200px;text-align:center}
.visit h2{font-family:var(--serif);font-weight:400;font-size:20px;color:var(--heading);margin-bottom:5px}
.visit li{list-style:none;font-size:14.5px;line-height:30px}
.divider{position:absolute;left:113px;top:804px;width:971px;height:1px;background:#d8d6d7}
.services{position:absolute;left:129px;top:827px}
.services h2{font-family:var(--serif);font-weight:400;font-size:20px;color:var(--heading);margin-bottom:8px}
.services li{list-style:none;font-size:12.5px;line-height:24px;padding-left:1px}
.services-sep{position:absolute;left:805px;top:835px;width:2px;height:235px;background:linear-gradient(transparent,#c9c7c8 30%,#c9c7c8 70%,transparent)}
.phone-card{position:absolute;left:807px;top:907px;width:277px;height:88px;border-radius:0 12px 12px 0;background:linear-gradient(#86c8dc,#4aa5c4);display:flex;align-items:center;padding-left:18px;color:var(--white);font-family:var(--serif);font-size:32px}
.phone-card svg{margin-right:10px}
.emergency{position:absolute;left:825px;top:1003px;font-size:14.5px;line-height:20px;color:#7a7a7a}
.footer-rule{position:absolute;left:0;top:1100px;width:1200px;height:6px;background:var(--rule)}
.footer{position:absolute;left:0;top:1106px;width:1200px;height:94px;background:var(--navy);color:var(--white);text-align:center}
.footer-nav{margin-top:31px;font-size:12.5px}
.footer-nav .sep{margin:0 8px}
.copyright{margin-top:6px;font-size:11.5px}
</style>
</head>
<body>
<div class="brand">DrVantrell</div>
<header class="masthead"></header>
<div class="masthead-rule"></div>
<nav class="main-nav">
  <a class="is-current" href="#">Home</a><span class="sep">|</span>
  <a href="#">Why we are different</a><span class="sep">|</span>
  <a href="#">Technologies we offer</a><span class="sep">|</span>
  <a href="#">Meet Dr. Vantrell</a><span class="sep">|</span>
  <a href="#">Our Staff</a><span class="sep">|</span>
  <a href="#">Contact Us</a>
</nav>

<section class="intro">
  <div class="intro-photo" role="img" aria-label="Photo of the dental office building among trees"></div>
  <p>Lorem ipsum dolor sit amet, consectetur adipiscing elit. Aenean leo ipsum, molestie non aliquam a, fringilla vel lectus. Cum sociis natoque penatibus et magnis dis parturient montes, nascetur ridiculus mus. Suspendisse aliquet nisi sed massa porttitor id scelerisque mi rhoncus Cum sociis natoque penatibus et magnis dis parturient montes.</p>
  <p>Donec consectetur varius facilisis. Phasellus scelerisque molestie nulla, vitae mattis velit egestas ac. Vestibulum ante ipsum primis in faucibus orci luctus et ultrices posuere cubilia. Maecenas tincidunt ultrices risus, id luctus tellus semper eu. Pellentesque eros neque, egestas sit amet imperdiet vitae, gravida nec libero. Cras accumsan velit quis tellus varius pretium.</p>
</section>
<div class="section-rule"></div>
<svg class="pointer" width="180" height="86" viewBox="0 0 180 86">
  <defs><linearGradient id="pointerFill" x1="0" y1="0" x2="0" y2="1"><stop offset="0" stop-color="#a9a9ab"/><stop offset="1" stop-color="#f2f1f2"/></linearGradient></defs>
  <polygon points="0,0 180,0 90,84" fill="url(#pointerFill)"/>
</svg>

<div class="col" style="left:123px"><h2>Education</h2><ul>
<li>Emergency Dental Care</li><li>Your Mouth</li><li>Your Tooth</li><li>Cracked Tooth?</li><li>Missing a Tooth?</li><li>Sensitive Teeth</li><li>Dry Mouth</li><li>Tooth Grinding</li><li>Sleep Dentistry</li><li>Videos</li></ul></div>
<div class="col" style="left:314px"><h2>Prevetive</h2><ul>
<li>What is Preventive Care?</li><li>Taking Care of Your Teeth</li><li>Eating Right</li><li>Dental Check-Ups</li><li>Sealants</li><li>Periodontal Disease</li><li>Kicking the Habit</li><li>Night Guards</li><li>Dental X-Rays</li><li>Antibiotics with Treatment</li></ul></div>
<div class="visit"><h2>Visiting our office</h2><ul>
<li>Where to Stay</li><li>First Visit / Map</li><li>Financial Policy</li><li>Dental Insurance</li></ul></div>
<div class="col" style="left:741px"><h2>Restorations</h2><ul>
<li>Crowns/Caps: Each Step</li><li>CMBRs</li><li>Porcelain Bridges</li><li>Bonded Dental Bridges</li><li>Gold Restorations</li><li>Implants</li><li>Treating Cracked Teeth</li><li>Periodontal (gum) Treatment</li></ul></div>
<div class="col" style="left:935px"><h2>Cosmetics</h2><ul>
<li>Cosmetic Dentistry</li><li>Bleaching and Whitening</li><li>Cosmetic Bonding</li><li>Esthetic Veneers</li><li>Tooth Shaping</li></ul></div>

<div class="divider"></div>
<section class="services"><h2>Dr. Vantrell Provides</h2><ul>
<li>General dentistry—oral hygiene, cavity detection and repair, crowns.</li>
<li>Cosmetic/restorative dentistry—broken or misshapen teeth, crooked smiles, unsightly gaps</li>
<li>Non-metal fillings—nontoxic, durable tooth-colored resin fillings that are proven to provide better results</li>
<li>Tooth shaping—extending, shortening or otherwise reshaping teeth for improved esthetics</li>
<li>Complete smile make-over's—resin veneers that reshape the whole mouth while preserving natural teeth</li>
<li>Tooth whitening—at-home bleaching options to make teeth appear years younger</li>
<li>Laser Dentistry, Sleep Dentistry, and Implant Dentistry with the Finest and Latest Equipment and Materials.</li>
<li>Dental Implants to replace missing teeth.</li>
<li>Sedation Dentistry so you can be relaxed.</li></ul></section>
<div class="services-sep"></div>
<div class="phone-card">
  <svg width="26" height="58" viewBox="0 0 26 58"><path d="M20 3 C8 4 2 14 2 29 C2 44 8 54 20 55 L23 46 C17 44 13 38 13 29 C13 20 17 14 23 12 Z" fill="#5aa9c2" stroke="#3b8aa6" stroke-width="1.5"/></svg>
  <span>(707) 555-0143</span>
</div>
<p class="emergency">in case of emergency<br>call (707) 555-0178</p>

<div class="footer-rule"></div>
<footer class="footer">
  <nav class="footer-nav">Home<span class="sep">|</span>Why we are different<span class="sep">|</span>Technologies we offer<span class="sep">|</span>Meet Dr. Vantrell<span class="sep">|</span>Our Staff<span class="sep">|</span>Contact Us</nav>
  <p class="copyright">Copyright © 2010 drvantrell.example</p>
</footer>
</body>
</html>
```